Ladles and Lanterns App design

I need a full app design, colours, images, fonts, and a mock up design of the app to bring to the developer.

Ladles and Lanterns is a free app that allows cafes, independent cafe and chains of cafes to let their customers know what the soup of the day and what specials they have on that day through the app. Each cafe will have a profile which they can upload the Ladles and Lanterns daily.

The user home screen will include google maps showing their location with the registered cafes and eateries around them. including a list of the cafe and distances below. as seen in attachment.

Target Market(s)

Cafes , anyone who enjoys eating soups and off local cafe specials boards

Requirements
Must have
• I would like a complete app design based on the attached images.

```html
<!DOCTYPE html>
<html lang="en">
<head>
<meta charset="utf-8">
<title>Ladles and Lanterns – App Screens</title>
<link href="https://fonts.googleapis.com/css2?family=Poppins:wght@400;500;600;700&display=swap" rel="stylesheet">
<style>
:root{
  --canvas:#eeeeee;
  --surface:#ffffff;
  --orange:#f4511e;
  --ink:#2b2b2b;
  --muted:#9a9a9a;
  --faint:#c9c9c9;
  --line:#ececec;
  --green:#3cc35f;
  --red:#f0533a;
  --heart:#e8412c;
  --icon:#bbbbbb;
}
*{box-sizing:border-box;margin:0;padding:0}
html,body{width:1200px;height:2580px;overflow:hidden}
body{background:var(--canvas);font-family:"Poppins",sans-serif;color:var(--ink);position:relative}

.screen{position:absolute;width:360px;background:var(--surface);overflow:hidden;display:flex;flex-direction:column;box-shadow:0 6px 18px rgba(0,0,0,.06)}
.col-left{left:208px}.col-right{left:648px}
.row-1{top:88px;height:652px}
.row-2{top:832px;height:628px}
.row-3{top:1528px;height:962px}

.photo-hero{flex:1;background:linear-gradient(160deg,#3b3530 0%,#6a5540 40%,#b58d3e 62%,#4a3d32 85%,#2f2a26 100%)}

.map-area{position:relative;flex:1;background:linear-gradient(160deg,#eef0ea,#e2e7dc 55%,#ebeee6)}
.map-placeholder{position:absolute;inset:0}

.shop-card{background:var(--surface);border-radius:6px;display:flex;align-items:flex-start;gap:14px;padding:16px 16px 14px}
.map-area .shop-card{position:absolute;left:14px;right:14px;bottom:22px;box-shadow:0 6px 16px rgba(0,0,0,.12)}
.avatar{width:48px;height:48px;border-radius:50%;flex:none;background:radial-gradient(circle,#c99a45 0%,#7a5a3a 60%,#4a3a30 100%)}
.shop-info{flex:1;padding-top:6px;min-width:0}
.shop-name{font-size:14px;font-weight:500;color:var(--ink);white-space:nowrap}
.shop-type{font-size:11px;color:var(--muted);margin-top:2px}
.shop-meta{display:flex;flex-direction:column;align-items:flex-end;justify-content:space-between;height:52px;padding-top:6px;flex:none}
.shop-dist{font-size:9px;color:var(--muted)}

.appbar{height:58px;background:var(--orange);display:flex;align-items:center;justify-content:space-between;padding:0 18px;color:#fff;flex:none}
.appbar h1{font-size:15px;font-weight:600;letter-spacing:.5px;text-transform:uppercase}

.tabbar{height:72px;display:flex;border-top:1px solid var(--line);background:var(--surface);flex:none}
.tab{flex:1;display:flex;flex-direction:column;align-items:center;justify-content:center;gap:6px;font-size:10px;color:var(--muted)}
.tab svg{stroke:var(--muted)}
.tab.is-active{background:var(--orange);color:#fff}
.tab.is-active svg{stroke:#fff}

.list{flex:1;padding:6px 14px;overflow:hidden}
.soup-row{display:flex;align-items:center;gap:14px;height:88px;border-bottom:1px solid var(--line)}
.thumb{width:60px;height:60px;border-radius:3px;flex:none;background:linear-gradient(135deg,#4a5a3d,#8a7a45 55%,#d9a441)}
.soup-name{flex:1;font-size:14px;color:var(--ink);line-height:1.3}
.is-faded .soup-name{color:var(--faint)}
.is-faded .thumb{opacity:.45}

.search{margin:14px 14px 4px;height:42px;border-bottom:1px solid var(--line);display:flex;align-items:center;justify-content:space-between;font-size:12px;color:var(--muted);padding:0 6px;flex:none}
.section-label{font-size:13px;font-weight:500;padding:16px 0 4px;color:var(--ink)}
.toggle{width:14px;height:14px;border-radius:50%;flex:none;display:flex;align-items:center;justify-content:center}
.toggle.on{background:var(--green)}.toggle.off{background:var(--red)}
.toggle::after{content:"";width:6px;height:2px;background:#fff}

.shop-heading{display:flex;align-items:center;gap:8px;font-size:13px;font-weight:500;padding:14px 20px 6px;flex:none}
.shop-list{flex:1;padding:4px 14px;overflow:hidden}
.shop-list .shop-card{margin:10px 0;box-shadow:0 4px 12px rgba(0,0,0,.08);padding:18px 16px}
</style>
</head>
<body>

<!-- Splash -->
<section class="screen col-left row-1">
  <div class="photo-hero" role="img" aria-label="Overhead photograph of bowls of golden chicken soup with herbs on a dark wooden table"></div>
</section>

<!-- Home map -->
<section class="screen col-right row-1">
  <div class="map-area">
    <div class="map-placeholder" role="img" aria-label="Map of the user's location with nearby registered cafes marked"></div>
    <div class="shop-card">
      <div class="avatar" role="img" aria-label="Photo of a bowl of soup"></div>
      <div class="shop-info"><div class="shop-name">Hearthside Soup Co.</div><div class="shop-type">Soup Restaurant</div></div>
      <div class="shop-meta"><span class="shop-dist">1.2 km</span>
        <svg width="16" height="14" viewBox="0 0 16 14" fill="none" stroke="#f4511e" stroke-width="2"><path d="M1 7h13M9 2l5 5-5 5"/></svg></div>
    </div>
  </div>
  <nav class="tabbar">
    <div class="tab"><svg width="22" height="20" viewBox="0 0 22 20" fill="none" stroke-width="1.6"><path d="M2 9h18a9 9 0 0 1-18 0zM7 5v-3M11 5v-4M15 5v-3"/></svg>Soup</div>
    <div class="tab"><svg width="20" height="20" viewBox="0 0 20 20" fill="none" stroke-width="1.6"><path d="M2 10V2h8l8 8-8 8z"/><circle cx="6" cy="6" r="1.5"/></svg>Specials</div>
    <div class="tab"><svg width="20" height="20" viewBox="0 0 20 20" fill="none" stroke-width="1.6"><circle cx="10" cy="6" r="4"/><path d="M2 19c0-4 4-6 8-6s8 2 8 6"/></svg>Account</div>
    <div class="tab"><svg width="20" height="20" viewBox="0 0 20 20" fill="none" stroke-width="1.6"><circle cx="10" cy="10" r="3"/><path d="M10 1v3M10 16v3M1 10h3M16 10h3M3.6 3.6l2 2M14.4 14.4l2 2M3.6 16.4l2-2M14.4 5.6l2-2"/></svg>Settings</div>
  </nav>
</section>

<!-- Soups type -->
<section class="screen col-left row-2">
  <header class="appbar">
    <svg width="18" height="16" viewBox="0 0 18 16" fill="none" stroke="#fff" stroke-width="2"><path d="M17 8H2M7 2 1 8l6 6"/></svg>
    <h1>Soups Type</h1>
    <svg width="18" height="18" viewBox="0 0 18 18" fill="#fff"><path d="M9 1 1 8h2v9h4v-5h4v5h4V8h2z"/></svg>
  </header>
  <div class="list">
    <div class="soup-row"><div class="thumb" role="img" aria-label="Chicken noodle soup"></div><div class="soup-name">Chicken Noodle<br>Soup</div><svg width="18" height="16" viewBox="0 0 18 16" fill="none" stroke="#bbb" stroke-width="1.5"><path d="M9 15S1 10 1 5a4 4 0 0 1 8-1 4 4 0 0 1 8 1c0 5-8 10-8 10z"/></svg></div>
    <div class="soup-row"><div class="thumb" role="img" aria-label="Tortilla soup"></div><div class="soup-name">Tortilla Soup</div><svg width="18" height="16" viewBox="0 0 18 16" fill="#e8412c"><path d="M9 15S1 10 1 5a4 4 0 0 1 8-1 4 4 0 0 1 8 1c0 5-8 10-8 10z"/></svg></div>
    <div class="soup-row"><div class="thumb" role="img" aria-label="Slow cooker soup"></div><div class="soup-name">Slow Cooker Soup</div><svg width="18" height="16" viewBox="0 0 18 16" fill="none" stroke="#bbb" stroke-width="1.5"><path d="M9 15S1 10 1 5a4 4 0 0 1 8-1 4 4 0 0 1 8 1c0 5-8 10-8 10z"/></svg></div>
    <div class="soup-row"><div class="thumb" role="img" aria-label="Cream soup"></div><div class="soup-name">Cream Soups</div><svg width="18" height="16" viewBox="0 0 18 16" fill="none" stroke="#bbb" stroke-width="1.5"><path d="M9 15S1 10 1 5a4 4 0 0 1 8-1 4 4 0 0 1 8 1c0 5-8 10-8 10z"/></svg></div>
    <div class="soup-row"><div class="thumb" role="img" aria-label="Bean and pea soup"></div><div class="soup-name">Bean &amp; Pea Soups</div><svg width="18" height="16" viewBox="0 0 18 16" fill="none" stroke="#bbb" stroke-width="1.5"><path d="M9 15S1 10 1 5a4 4 0 0 1 8-1 4 4 0 0 1 8 1c0 5-8 10-8 10z"/></svg></div>
  </div>
  <nav class="tabbar">
    <div class="tab is-active"><svg width="22" height="20" viewBox="0 0 22 20" fill="none" stroke-width="1.6"><path d="M2 9h18a9 9 0 0 1-18 0zM7 5v-3M11 5v-4M15 5v-3"/></svg>Soup</div>
    <div class="tab"><svg width="20" height="20" viewBox="0 0 20 20" fill="none" stroke-width="1.6"><path d="M2 10V2h8l8 8-8 8z"/><circle cx="6" cy="6" r="1.5"/></svg>Specials</div>
    <div class="tab"><svg width="20" height="18" viewBox="0 0 20 18" fill="none" stroke-width="1.6"><path d="M10 17S1 11 1 5.5a4.5 4.5 0 0 1 9-1 4.5 4.5 0 0 1 9 1C19 11 10 17 10 17z"/></svg>Favorites</div>
    <div class="tab"><svg width="20" height="20" viewBox="0 0 20 20" fill="none" stroke-width="1.6"><circle cx="10" cy="10" r="3"/><path d="M10 1v3M10 16v3M1 10h3M16 10h3M3.6 3.6l2 2M14.4 14.4l2 2M3.6 16.4l2-2M14.4 5.6l2-2"/></svg>Settings</div>
  </nav>
</section>

<!-- Specials soups -->
<section class="screen col-right row-2">
  <header class="appbar">
    <svg width="18" height="16" viewBox="0 0 18 16" fill="none" stroke="#fff" stroke-width="2"><path d="M17 8H2M7 2 1 8l6 6"/></svg>
    <h1>Specials Soups</h1>
    <svg width="18" height="18" viewBox="0 0 18 18" fill="#fff"><path d="M9 1 1 8h2v9h4v-5h4v5h4V8h2z"/></svg>
  </header>
  <div class="list">
    <div class="soup-row"><div class="thumb" role="img" aria-label="Chicken noodle soup"></div><div class="soup-name">Chicken Noodle<br>Soup</div><svg width="18" height="16" viewBox="0 0 18 16" fill="none" stroke="#bbb" stroke-width="1.5"><path d="M9 15S1 10 1 5a4 4 0 0 1 8-1 4 4 0 0 1 8 1c0 5-8 10-8 10z"/></svg></div>
    <div class="soup-row"><div class="thumb" role="img" aria-label="Tortilla soup"></div><div class="soup-name">Tortilla Soup</div><svg width="18" height="16" viewBox="0 0 18 16" fill="#e8412c"><path d="M9 15S1 10 1 5a4 4 0 0 1 8-1 4 4 0 0 1 8 1c0 5-8 10-8 10z"/></svg></div>
    <div class="soup-row"><div class="thumb" role="img" aria-label="Slow cooker soup"></div><div class="soup-name">Slow Cooker Soup</div><svg width="18" height="16" viewBox="0 0 18 16" fill="none" stroke="#bbb" stroke-width="1.5"><path d="M9 15S1 10 1 5a4 4 0 0 1 8-1 4 4 0 0 1 8 1c0 5-8 10-8 10z"/></svg></div>
    <div class="soup-row"><div class="thumb" role="img" aria-label="Cream soup"></div><div class="soup-name">Cream Soups</div><svg width="18" height="16" viewBox="0 0 18 16" fill="none" stroke="#bbb" stroke-width="1.5"><path d="M9 15S1 10 1 5a4 4 0 0 1 8-1 4 4 0 0 1 8 1c0 5-8 10-8 10z"/></svg></div>
    <div class="soup-row"><div class="thumb" role="img" aria-label="Bean and pea soup"></div><div class="soup-name">Bean &amp; Pea Soups</div><svg width="18" height="16" viewBox="0 0 18 16" fill="none" stroke="#bbb" stroke-width="1.5"><path d="M9 15S1 10 1 5a4 4 0 0 1 8-1 4 4 0 0 1 8 1c0 5-8 10-8 10z"/></svg></div>
  </div>
  <nav class="tabbar">
    <div class="tab"><svg width="22" height="20" viewBox="0 0 22 20" fill="none" stroke-width="1.6"><path d="M2 9h18a9 9 0 0 1-18 0zM7 5v-3M11 5v-4M15 5v-3"/></svg>Soup</div>
    <div class="tab is-active"><svg width="20" height="20" viewBox="0 0 20 20" fill="none" stroke-width="1.6"><path d="M2 10V2h8l8 8-8 8z"/><circle cx="6" cy="6" r="1.5"/></svg>Specials</div>
    <div class="tab"><svg width="20" height="18" viewBox="0 0 20 18" fill="none" stroke-width="1.6"><path d="M10 17S1 11 1 5.5a4.5 4.5 0 0 1 9-1 4.5 4.5 0 0 1 9 1C19 11 10 17 10 17z"/></svg>Favorites</div>
    <div class="tab"><svg width="20" height="20" viewBox="0 0 20 20" fill="none" stroke-width="1.6"><circle cx="10" cy="10" r="3"/><path d="M10 1v3M10 16v3M1 10h3M16 10h3M3.6 3.6l2 2M14.4 14.4l2 2M3.6 16.4l2-2M14.4 5.6l2-2"/></svg>Settings</div>
  </nav>
</section>

<!-- Favorites -->
<section class="screen col-left row-3">
  <header class="appbar">
    <svg width="18" height="16" viewBox="0 0 18 16" fill="none" stroke="#fff" stroke-width="2"><path d="M17 8H2M7 2 1 8l6 6"/></svg>
    <h1>Favorites Soups</h1>
    <svg width="18" height="18" viewBox="0 0 18 18" fill="#fff"><path d="M9 1 1 8h2v9h4v-5h4v5h4V8h2z"/></svg>
  </header>
  <div class="search"><span>Search here...</span><svg width="14" height="14" viewBox="0 0 14 14" fill="none" stroke="#9a9a9a" stroke-width="1.6"><circle cx="6" cy="6" r="4.5"/><path d="m9.5 9.5 3.5 3.5"/></svg></div>
  <div class="list">
    <div class="section-label">Soups</div>
    <div class="soup-row"><div class="thumb" role="img" aria-label="Chicken noodle soup"></div><svg width="18" height="16" viewBox="0 0 18 16" fill="none" stroke="#444" stroke-width="1.5"><path d="M9 15S1 10 1 5a4 4 0 0 1 8-1 4 4 0 0 1 8 1c0 5-8 10-8 10z"/></svg><div class="soup-name">Chicken Noodle<br>Soup</div><span class="toggle on"></span></div>
    <div class="soup-row is-faded"><div class="thumb" role="img" aria-label="Tortilla soup"></div><svg width="18" height="16" viewBox="0 0 18 16" fill="none" stroke="#ccc" stroke-width="1.5"><path d="M9 15S1 10 1 5a4 4 0 0 1 8-1 4 4 0 0 1 8 1c0 5-8 10-8 10z"/></svg><div class="soup-name">Tortilla Soup</div><span class="toggle off"></span></div>
    <div class="soup-row"><div class="thumb" role="img" aria-label="Slow cooker soup"></div><svg width="18" height="16" viewBox="0 0 18 16" fill="none" stroke="#444" stroke-width="1.5"><path d="M9 15S1 10 1 5a4 4 0 0 1 8-1 4 4 0 0 1 8 1c0 5-8 10-8 10z"/></svg><div class="soup-name">Slow Cooker Soup</div><span class="toggle on"></span></div>
    <div class="soup-row"><div class="thumb" role="img" aria-label="Cream soup"></div><svg width="18" height="16" viewBox="0 0 18 16" fill="none" stroke="#444" stroke-width="1.5"><path d="M9 15S1 10 1 5a4 4 0 0 1 8-1 4 4 0 0 1 8 1c0 5-8 10-8 10z"/></svg><div class="soup-name">Cream Soups</div><span class="toggle off"></span></div>
    <div class="section-label">Specials</div>
    <div class="soup-row is-faded"><div class="thumb" role="img" aria-label="Tortilla soup"></div><svg width="18" height="16" viewBox="0 0 18 16" fill="none" stroke="#ccc" stroke-width="1.5"><path d="M9 15S1 10 1 5a4 4 0 0 1 8-1 4 4 0 0 1 8 1c0 5-8 10-8 10z"/></svg><div class="soup-name">Tortilla Soup</div><span class="toggle off"></span></div>
    <div class="soup-row"><div class="thumb" role="img" aria-label="Slow cooker soup"></div><svg width="18" height="16" viewBox="0 0 18 16" fill="none" stroke="#444" stroke-width="1.5"><path d="M9 15S1 10 1 5a4 4 0 0 1 8-1 4 4 0 0 1 8 1c0 5-8 10-8 10z"/></svg><div class="soup-name">Slow Cooker Soup</div><span class="toggle on"></span></div>
    <div class="soup-row"><div class="thumb" role="img" aria-label="Chicken noodle soup"></div><svg width="18" height="16" viewBox="0 0 18 16" fill="none" stroke="#444" stroke-width="1.5"><path d="M9 15S1 10 1 5a4 4 0 0 1 8-1 4 4 0 0 1 8 1c0 5-8 10-8 10z"/></svg><div class="soup-name">Chicken Noodle<br>Soup</div><span class="toggle on"></span></div>
  </div>
  <nav class="tabbar">
    <div class="tab"><svg width="22" height="20" viewBox="0 0 22 20" fill="none" stroke-width="1.6"><path d="M2 9h18a9 9 0 0 1-18 0zM7 5v-3M11 5v-4M15 5v-3"/></svg>Soup</div>
    <div class="tab"><svg width="20" height="20" viewBox="0 0 20 20" fill="none" stroke-width="1.6"><path d="M2 10V2h8l8 8-8 8z"/><circle cx="6" cy="6" r="1.5"/></svg>Specials</div>
    <div class="tab is-active"><svg width="20" height="18" viewBox="0 0 20 18" fill="none" stroke-width="1.6"><path d="M10 17S1 11 1 5.5a4.5 4.5 0 0 1 9-1 4.5 4.5 0 0 1 9 1C19 11 10 17 10 17z"/></svg>Favorites</div>
    <div class="tab"><svg width="20" height="20" viewBox="0 0 20 20" fill="none" stroke-width="1.6"><circle cx="10" cy="10" r="3"/><path d="M10 1v3M10 16v3M1 10h3M16 10h3M3.6 3.6l2 2M14.4 14.4l2 2M3.6 16.4l2-2M14.4 5.6l2-2"/></svg>Settings</div>
  </nav>
</section>

<!-- Soup shop -->
<section class="screen col-right row-3">
  <header class="appbar">
    <svg width="18" height="16" viewBox="0 0 18 16" fill="none" stroke="#fff" stroke-width="2"><path d="M17 8H2M7 2 1 8l6 6"/></svg>
    <h1>Soup Shop</h1>
    <svg width="18" height="18" viewBox="0 0 18 18" fill="#fff"><path d="M9 1 1 8h2v9h4v-5h4v5h4V8h2z"/></svg>
  </header>
  <div class="search"><span>Search here...</span><svg width="14" height="14" viewBox="0 0 14 14" fill="none" stroke="#9a9a9a" stroke-width="1.6"><circle cx="6" cy="6" r="4.5"/><path d="m9.5 9.5 3.5 3.5"/></svg></div>
  <div class="shop-heading"><span class="toggle on"></span>Chicken Noodle Soup</div>
  <div class="shop-list">
    <div class="shop-card"><div class="avatar" role="img" aria-label="Photo of a bowl of soup"></div><div class="shop-info"><div class="shop-name">Hearthside Soup Co.</div><div class="shop-type">Soup Restaurant</div></div><div class="shop-meta"><span class="shop-dist">0.8 km</span><svg width="16" height="14" viewBox="0 0 16 14" fill="none" stroke="#f4511e" stroke-width="2"><path d="M1 7h13M9 2l5 5-5 5"/></svg></div></div>
    <div class="shop-card"><div class="avatar" role="img" aria-label="Photo of a bowl of soup"></div><div class="shop-info"><div class="shop-name">Hearthside Soup Co.</div><div class="shop-type">Soup Restaurant</div></div><div class="shop-meta"><span class="shop-dist">1.2 km</span><svg width="16" height="14" viewBox="0 0 16 14" fill="none" stroke="#f4511e" stroke-width="2"><path d="M1 7h13M9 2l5 5-5 5"/></svg></div></div>
    <div class="shop-card"><div class="avatar" role="img" aria-label="Photo of a bowl of soup"></div><div class="shop-info"><div class="shop-name">Hearthside Soup Co.</div><div class="shop-type">Soup Restaurant</div></div><div class="shop-meta"><span class="shop-dist">1.9 km</span><svg width="16" height="14" viewBox="0 0 16 14" fill="none" stroke="#f4511e" stroke-width="2"><path d="M1 7h13M9 2l5 5-5 5"/></svg></div></div>
    <div class="shop-card"><div class="avatar" role="img" aria-label="Photo of a bowl of soup"></div><div class="shop-info"><div class="shop-name">Hearthside Soup Co.</div><div class="shop-type">Soup Restaurant</div></div><div class="shop-meta"><span class="shop-dist">2.4 km</span><svg width="16" height="14" viewBox="0 0 16 14" fill="none" stroke="#f4511e" stroke-width="2"><path d="M1 7h13M9 2l5 5-5 5"/></svg></div></div>
    <div class="shop-card"><div class="avatar" role="img" aria-label="Photo of a bowl of soup"></div><div class="shop-info"><div class="shop-name">Hearthside Soup Co.</div><div class="shop-type">Soup Restaurant</div></div><div class="shop-meta"><span class="shop-dist">3.1 km</span><svg width="16" height="14" viewBox="0 0 16 14" fill="none" stroke="#f4511e" stroke-width="2"><path d="M1 7h13M9 2l5 5-5 5"/></svg></div></div>
  </div>
  <nav class="tabbar">
    <div class="tab"><svg width="22" height="20" viewBox="0 0 22 20" fill="none" stroke-width="1.6"><path d="M2 9h18a9 9 0 0 1-18 0zM7 5v-3M11 5v-4M15 5v-3"/></svg>Soup</div>
    <div class="tab"><svg width="20" height="20" viewBox="0 0 20 20" fill="none" stroke-width="1.6"><path d="M2 10V2h8l8 8-8 8z"/><circle cx="6" cy="6" r="1.5"/></svg>Specials</div>
    <div class="tab is-active"><svg width="20" height="18" viewBox="0 0 20 18" fill="none" stroke-width="1.6"><path d="M10 17S1 11 1 5.5a4.5 4.5 0 0 1 9-1 4.5 4.5 0 0 1 9 1C19 11 10 17 10 17z"/></svg>Favorites</div>
    <div class="tab"><svg width="20" height="20" viewBox="0 0 20 20" fill="none" stroke-width="1.6"><circle cx="10" cy="10" r="3"/><path d="M10 1v3M10 16v3M1 10h3M16 10h3M3.6 3.6l2 2M14.4 14.4l2 2M3.6 16.4l2-2M14.4 5.6l2-2"/></svg>Settings</div>
  </nav>
</section>

</body>
</html>
```